Global Aviation Services website

we are a start up airline/aviation services company that will operate in Australia, USA and New Zealand initially. Fundamentally the service is to airlines who fly into and out of a market yet do not wish to have their own admin, sales and marketing infrastructures. They would use us.
The company name is Veltaro.
It needs to look sophisticated, sharp and professional. We would like it designed and built in the CMS - wordpress so we can update after the project is finished when necessary. An example of who we are and a good website we like can be found at: http://pembrikegroup.example/. There is no ecommerce or interactivity other than a contact us. We do like animation for promotion. There will be links to our airline clients and sub sites or pages will exist for the various offices we have globally. Currently 6. Each of these offices will have a dedicated local URL. Please submit your suggestion of a home page and 2 internal pages. Thank you and kind regards Miriam
Target Market(s)
airlines, airline technology companies,
Industry/Entity Type
Aviation
Coding
Coded - Design and coding required
Number of Pages Required
5+ page
Look and feel

```html
<!DOCTYPE html>
<html lang="en">
<head>
<meta charset="utf-8">
<title>Veltaro — Global Aviation Services</title>
<link rel="stylesheet" href="https://fonts.googleapis.com/css2?family=Arimo:wght@400;700&family=Roboto+Condensed:wght@400;700&family=Roboto+Slab:wght@400&family=Montserrat:wght@700&display=swap">
<style>
  :root {
    --purple: #6a3f98;
    --purple-dark: #53307a;
    --red: #e11f26;
    --red-line: #d32027;
    --ink: #333;
    --grey-bg: #efefef;
    --rule: #cfcfcf;
    --footer: #3a3a3a;
    --white: #fff;
  }
  * { box-sizing: border-box; margin: 0; padding: 0; }
  html, body { width: 704px; height: 1200px; overflow: hidden; background: var(--white); }
  body { position: relative; font-family: "Arimo", Arial, sans-serif; color: var(--ink); }
  .abs { position: absolute; }

  .topbar { left: 0; top: 0; width: 704px; height: 20px; background: var(--purple); color: var(--white);
    font: 8.5px/18px "Roboto Slab", serif; text-align: center; border-bottom: 2px solid #4a2a70; }

  .brand { font-family: "Montserrat", sans-serif; font-weight: 700; color: var(--purple); letter-spacing: 1px; }
  .header-brand { left: 50px; top: 30px; font-size: 32px; line-height: 40px; }
  .header-phone { left: 554px; top: 30px; font-size: 12px; line-height: 16px; color: #333; display: flex; align-items: center; gap: 5px; }
  .nav { left: 336px; top: 62px; display: flex; font: 9.5px/14px "Roboto Slab", serif; color: #333; }
  .nav a { color: inherit; text-decoration: none; padding: 0 15px; border-left: 1px solid #888; }
  .nav a:first-child { border-left: 0; color: var(--purple); }

  .hero { left: 0; top: 82px; width: 704px; height: 263px;
    background: linear-gradient(160deg, #c9dbe9 0%, #6f9cc4 30%, #1f4f86 60%, #2c5d92 80%, #e3a24f 100%); }
  .hero-caption { left: 0; top: 307px; width: 704px; height: 38px; background: rgba(20,25,35,.75); color: var(--white);
    font: 14.5px/17px "Roboto Condensed", sans-serif; text-align: center; padding-top: 3px; }
  .hero-arrow { width: 20px; height: 22px; background: #222; display: flex; align-items: center; justify-content: center; }

  .section-title { width: 704px; left: 0; text-align: center; font: 16px/20px "Roboto Slab", serif; color: var(--purple); }
  .rule { left: 120px; width: 464px; height: 1px; background: var(--rule); }
  .rule::after { content: ""; position: absolute; left: 191px; top: -1px; width: 82px; height: 3px; background: var(--red-line); }

  .welcome-text { left: 62px; top: 402px; width: 580px; font-size: 8px; line-height: 13px; text-align: center; color: #333; }
  .read-more { left: 0; width: 704px; top: 460px; text-align: center; font-size: 7.5px; color: var(--purple); text-decoration: underline; }

  .services-bg { left: 0; top: 494px; width: 704px; height: 284px; background: var(--grey-bg); }
  .card { top: 555px; width: 145px; height: 182px; background: var(--white); border: 1px solid #ccc; }
  .card-head { height: 22px; background: var(--purple); color: var(--white); font: 10px/22px "Roboto Condensed", sans-serif; padding-left: 5px; }
  .card-photo { position: absolute; left: 4px; top: 26px; width: 135px; height: 82px; }
  .card-text { position: absolute; left: 0; top: 112px; border-top: 1px solid #ccc; width: 143px; padding: 8px 5px 0; font-size: 7.5px; line-height: 11.5px; color: #333; }
  .card-plus { position: absolute; left: 64px; bottom: -9px; width: 16px; height: 16px; border-radius: 50%; background: var(--purple);
    color: var(--white); font: 12px/16px Arimo, sans-serif; text-align: center; }

  .client { top: 841px; width: 98px; height: 53px; background: #eaeaea; display: flex; align-items: center; justify-content: center; gap: 6px;
    color: #b5b5b5; font: 700 12px/11px "Roboto Condensed", sans-serif; }
  .client i { width: 14px; height: 14px; border-radius: 50%; background: #c8c8c8; display: block; }
  .client-arrow { top: 855px; color: #999; font: 22px/22px Arimo, sans-serif; }

  .cta { left: 0; top: 917px; width: 704px; height: 53px; background: var(--purple); }
  .cta-text { left: 57px; top: 925px; width: 440px; color: var(--white); font: 700 13px/19px "Roboto Condensed", sans-serif; }
  .cta-call { left: 504px; top: 924px; width: 133px; height: 38px; background: var(--red); color: var(--white); text-align: center;
    border-radius: 2px; font: 10px/12px Arimo, sans-serif; padding-top: 4px; }
  .cta-call strong { display: block; font-weight: 400; font-size: 15.5px; line-height: 18px; }

  .footer { left: 0; top: 970px; width: 704px; height: 208px; background: linear-gradient(135deg, #3f3f3f, #333); }
  .contact-title { left: 51px; top: 978px; color: var(--white); font: 400 12.5px/18px "Roboto Slab", serif; }
  .contact-rule { left: 51px; top: 1000px; width: 185px; height: 1px; background: #777; }
  .contact-rule::before { content: ""; position: absolute; left: 0; top: -1px; width: 48px; height: 2px; background: var(--red-line); }
  .contact-item { left: 57px; color: var(--white); font-size: 8.5px; line-height: 12px; display: flex; gap: 10px; }
  .contact-item svg { flex: none; margin-top: 1px; width: 12px; }
  .footer-brand { left: 272px; top: 1048px; font-size: 30px; color: var(--white); }

  .inquiry { left: 453px; top: 980px; width: 185px; height: 192px; background: rgba(90,90,90,.85); border-top: 2px solid var(--purple); }
  .inquiry-head { position: absolute; left: 10px; top: 10px; display: flex; align-items: center; gap: 8px; color: var(--white); font: 12px/20px "Roboto Slab", serif; }
  .inquiry-head span.icon { width: 22px; height: 22px; border-radius: 50%; background: var(--white); display: flex; align-items: center; justify-content: center; }
  .inquiry-lead { position: absolute; left: 9px; top: 46px; color: var(--white); font-size: 7.5px; }
  .field { position: absolute; left: 8px; width: 168px; height: 19px; background: #6d6d6d; border-bottom: 1px solid #888; color: #ddd; font-size: 7.5px; line-height: 19px; padding-left: 7px; }
  .submit { position: absolute; left: 8px; top: 160px; width: 70px; height: 19px; background: var(--red); color: var(--white); font: 700 10px/19px Arimo, sans-serif; text-align: center; }

  .bottombar { left: 0; top: 1178px; width: 704px; height: 22px; background: var(--purple); color: var(--white); font-size: 7.5px; line-height: 22px; text-align: center; }
</style>
</head>
<body>

<div class="abs topbar">We Are A Airline / Aviation Services Company That Will Operate In Australia, USA And New Zealand</div>

<header>
  <div class="abs brand header-brand">Veltaro</div>
  <div class="abs header-phone">
    <svg width="17" height="17" viewBox="0 0 20 20"><circle cx="10" cy="10" r="9" fill="none" stroke="#e11f26" stroke-width="1.5"/><path d="M7 5c-1 1-1 3 1 6s4 4 5 4l1-1-2-2-1 1c-1-1-2-2-3-4l1-1-2-3z" fill="#e11f26"/></svg>
    123-555-0178
  </div>
  <nav class="abs nav"><a href="#">Home</a><a href="#">About Us</a><a href="#">Our Services</a><a href="#">FAQ's</a><a href="#">Contact Us</a></nav>
</header>

<section>
  <div class="abs hero" role="img" aria-label="Glass office towers seen from below with an airliner flying overhead and business network graphics"></div>
  <div class="abs hero-arrow" style="left:4px;top:202px"><svg width="8" height="10" viewBox="0 0 8 10"><path d="M6 1 2 5l4 4" fill="none" stroke="#fff" stroke-width="2"/></svg></div>
  <div class="abs hero-arrow" style="left:676px;top:186px"><svg width="8" height="10" viewBox="0 0 8 10"><path d="M2 1l4 4-4 4" fill="none" stroke="#fff" stroke-width="2"/></svg></div>
  <div class="abs hero-caption">Our Service Is For The Airlines Who Fly Into And Out Of A Market Yet Do Not Wish To Have Their Own<br>Admin, Sales And Marketing Infrastructures</div>
</section>

<section>
  <div class="abs section-title" style="top:364px">Welcome to <span class="brand" style="font-size:16px">Veltaro</span></div>
  <div class="abs rule" style="top:392px"></div>
  <p class="abs welcome-text">Lorem ipsum dolor sit amet, consectetuer adipiscing elit, sed diam nonummy nibh euismod tincidunt ut laoreet dolore magna aliquam erat volutpat. Ut wisi enim ad minim veniam, quis nostrud exerci tation ullamcorper suscipit lobortis nisl ut aliquip ex ea commodo consequat. Duis autem vel eum iriure dolor in hendrerit in vulputate velit esse molestie consequat, vel illum dolore eu feugiat nulla facilisis at vero eros et accumsan et iusto odio dignissim qui blandit praesent luptatum zzril delenit augue duis dolore te feugait nulla facilisi.Lorem ipsum dolor sit amet, consectetuer</p>
  <div class="abs read-more">Read more</div>
</section>

<section>
  <div class="abs services-bg"></div>
  <div class="abs section-title" style="top:511px">Our Services</div>
  <div class="abs rule" style="top:537px"></div>

  <div class="abs card" style="left:55px">
    <div class="card-head">Admin Department</div>
    <div class="card-photo" role="img" aria-label="Airline staff member in uniform at an office desk" style="background:linear-gradient(180deg,#b9c3cf,#3a4250)"></div>
    <div class="card-text">Lorem ipsum dolor consectuer. Lorem ipsum dolor consectetuer ipsum dolor consectetuer. Lorem ipsum.consectuer. Lorem ipsum.</div>
    <div class="card-plus">+</div>
  </div>
  <div class="abs card" style="left:204px">
    <div class="card-head">Sales Service</div>
    <div class="card-photo" role="img" aria-label="Hand touching a sales chart on a transparent screen" style="background:linear-gradient(135deg,#dcdcdc,#6d7278)"></div>
    <div class="card-text">Lorem ipsum dolor consectuer. Lorem ipsum dolor consectetuer ipsum dolor consectetuer. Lorem ipsum.consectuer. Lorem ipsum.</div>
    <div class="card-plus">+</div>
  </div>
  <div class="abs card" style="left:354px">
    <div class="card-head">Marketing Infrastructures</div>
    <div class="card-photo" role="img" aria-label="Cargo aircraft on the apron at dusk" style="background:linear-gradient(180deg,#5d6f95,#c9a27a 70%,#4a4a4a)"></div>
    <div class="card-text">Lorem ipsum dolor consectuer. Lorem ipsum dolor consectetuer ipsum dolor consectetuer. Lorem ipsum.consectuer. Lorem ipsum.</div>
    <div class="card-plus">+</div>
  </div>
  <div class="abs card" style="left:503px">
    <div class="card-head">Ground Handling Services</div>
    <div class="card-photo" role="img" aria-label="Ground marshaller guiding a jet on the tarmac" style="background:linear-gradient(180deg,#4f7fc1,#a9c4e0 60%,#7c8a70)"></div>
    <div class="card-text">Lorem ipsum dolor consectuer. Lorem ipsum dolor consectetuer ipsum dolor consectetuer. Lorem ipsum.consectuer. Lorem ipsum.</div>
    <div class="card-plus">+</div>
  </div>
</section>

<section>
  <div class="abs section-title" style="top:800px">Our Airline Clients</div>
  <div class="abs rule" style="top:826px"></div>
  <div class="abs client-arrow" style="left:33px">&#8249;</div>
  <div class="abs client" style="left:55px"><i></i><span>LOGO<br>BRAND</span></div>
  <div class="abs client" style="left:179px"><i></i><span>LOGO<br>BRAND</span></div>
  <div class="abs client" style="left:302px"><i></i><span>LOGO<br>BRAND</span></div>
  <div class="abs client" style="left:426px"><i></i><span>LOGO<br>BRAND</span></div>
  <div class="abs client" style="left:550px"><i></i><span>LOGO<br>BRAND</span></div>
  <div class="abs client-arrow" style="left:660px">&#8250;</div>
</section>

<section>
  <div class="abs cta"></div>
  <p class="abs cta-text">Lorem ipsum dolor sit amet consectetur adipisicing elitsed do eiusmod tempor incididunt ut labore dolo magna aliqua.</p>
  <div class="abs cta-call">Call Us Today<strong>913-555-0146</strong></div>
</section>

<footer>
  <div class="abs footer" role="img" aria-label="Dark street map of the office neighbourhood"></div>
  <h2 class="abs contact-title">Contact Details</h2>
  <div class="abs contact-rule"></div>

  <div class="abs contact-item" style="top:1008px">
    <svg height="13" viewBox="0 0 10 13"><path d="M5 0a4.5 4.5 0 0 0-4.5 4.5C.5 8 5 13 5 13s4.5-5 4.5-8.5A4.5 4.5 0 0 0 5 0zm0 6.3a1.8 1.8 0 1 1 0-3.6 1.8 1.8 0 0 1 0 3.6z" fill="#fff"/></svg>
    <span>Postal Address<br>Street Name, City Name State Zip code</span></div>
  <div class="abs contact-item" style="top:1042px">
    <svg height="12" viewBox="0 0 10 12"><path d="M2 0c-2 1-2 4 0 7s5 5 7 5l1-2-2-2-1 1C5 8 4 7 3 5l1-1-1-3z" fill="#fff"/></svg>
    <span>Telephone<br>123-555-0178</span></div>
  <div class="abs contact-item" style="top:1075px">
    <svg height="11" viewBox="0 0 12 11"><rect x="3" y="0" width="6" height="3" fill="#fff"/><rect x="0" y="3" width="12" height="5" rx="1" fill="#fff"/><rect x="3" y="7" width="6" height="4" fill="#fff" stroke="#3a3a3a"/></svg>
    <span>Fax<br>124-555-0160</span></div>
  <div class="abs contact-item" style="top:1108px">
    <svg height="9" viewBox="0 0 10 8"><rect width="10" height="8" fill="#fff"/><path d="M0 0l5 4 5-4" fill="none" stroke="#3a3a3a"/></svg>
    <span>Email<br>Support: inquiry@veltaro.example</span></div>
  <div class="abs contact-item" style="top:1141px">
    <svg height="10" viewBox="0 0 10 10"><rect width="10" height="10" fill="#fff"/></svg>
    <span>Social<br>www.social.example/Veltaro</span></div>

  <div class="abs brand footer-brand">Veltaro</div>

  <form class="abs inquiry">
    <div class="inquiry-head"><span class="icon"><svg width="11" height="11" viewBox="0 0 10 12"><path d="M2 0c-2 1-2 4 0 7s5 5 7 5l1-2-2-2-1 1C5 8 4 7 3 5l1-1-1-3z" fill="#666"/></svg></span>Quick Inquiry</div>
    <p class="inquiry-lead">Lorem ipsum dolor sit amet, consectetuer</p>
    <div class="field" style="top:60px">Name</div>
    <div class="field" style="top:82px">Email</div>
    <div class="field" style="top:104px">Phone</div>
    <div class="field" style="top:126px;height:30px">Message</div>
    <div class="submit">SUBMIT</div>
  </form>

  <div class="abs bottombar">© 2016 Veltaro All rights reserved</div>
</footer>

</body>
</html>
```